Business Card Design Project

We need a simple business card design that uses our current logo.
We need to have the current logo put into a high res format.
We need to have 1 card made with contact information.
We will supply the information for the 4 employees.
Industry/Entity Type
Business
Requirements
Must have
- The contact information is as follows:
Paul Vardenko
Producer/CEO
c. 949-555-0148
f. 650-555-0193
paulv@lanternyardstudio.example
Mel Trosgaard, CFO
c. 949-555-0172
f. 650-555-0193
melt@lanternyardstudio.example
Paul Brenneky, PR
c. 267-555-0126
f. 650-555-0193
pbrenneky@lanternyardstudio.example
Dale Furnow, Producer
c. 949-555-0164
f. 650-555-0193
dalef@lanternyardstudio.example
The address for all cards is:
318 W Calle Norvista #2715, San Clemente, CA 92631

```html
<!DOCTYPE html>
<html lang="en">
<head>
<meta charset="utf-8">
<title>Lanternyard Studio — Dale Furnow, Producer</title>
<link rel="stylesheet" href="https://fonts.googleapis.com/css2?family=Cinzel:wght@600&family=Orbitron:wght@600&family=Tinos&display=swap">
<style>
  :root {
    --bg-top: #2c3550;
    --bg-mid: #55627f;
    --bg-right: #7c8aa2;
    --bg-bottom: #5d8a94;
    --panel-top: #12182a;
    --panel-mid: #1f2740;
    --panel-bottom: #4c7f8a;
    --strip: rgba(6, 10, 22, 0.45);
    --name-blue: #74b9f2;
    --brand-blue: #8fd0f5;
    --ink-light: #f2f4f8;
    --ornament-a: rgba(120, 160, 200, 0.35);
    --ornament-b: rgba(170, 70, 150, 0.30);
  }
  html, body {
    margin: 0;
    padding: 0;
    width: 1200px;
    height: 704px;
    overflow: hidden;
    background: #ffffff;
  }
  .card {
    position: relative;
    width: 1200px;
    height: 704px;
    overflow: hidden;
    background:
      radial-gradient(ellipse at 80% 25%, rgba(160,175,200,0.35), transparent 60%),
      linear-gradient(180deg, var(--bg-top) 0%, var(--bg-mid) 45%, var(--bg-right) 75%, var(--bg-bottom) 100%);
  }
  .side-panel {
    position: absolute;
    left: 0; top: 0;
    width: 525px; height: 704px;
    background: linear-gradient(180deg, var(--panel-top) 0%, var(--panel-mid) 45%, #3a4f68 75%, var(--panel-bottom) 100%);
    box-shadow: 8px 0 24px rgba(0,0,0,0.35);
  }
  .side-strip {
    position: absolute;
    left: 28px; top: 0;
    width: 450px; height: 704px;
    background: linear-gradient(180deg, var(--strip), rgba(6,10,22,0.1) 80%, transparent);
  }
  .ornament-left {
    position: absolute;
    left: 30px; top: 195px;
    width: 470px; height: 310px;
    border-radius: 40%;
    background: radial-gradient(ellipse at 40% 60%, var(--ornament-b), var(--ornament-a) 45%, transparent 72%);
  }
  .ornament-right {
    position: absolute;
    left: 930px; top: 260px;
    width: 270px; height: 300px;
    border-radius: 50%;
    background: radial-gradient(ellipse, rgba(150,170,210,0.25), transparent 70%);
  }
  .brand {
    position: absolute;
    left: 0; top: 312px;
    width: 525px;
    text-align: center;
    font-family: "Orbitron", sans-serif;
    font-weight: 600;
    font-size: 29px;
    color: var(--brand-blue);
    letter-spacing: 0.5px;
  }
  .person {
    position: absolute;
    left: 525px; top: 128px;
    width: 650px;
    text-align: center;
  }
  .person-name {
    margin: 0;
    font-family: "Cinzel", serif;
    font-weight: 600;
    font-size: 66px;
    line-height: 1;
    color: var(--name-blue);
    letter-spacing: 1px;
  }
  .person-title {
    margin: 14px 0 0;
    font-family: "Orbitron", sans-serif;
    font-weight: 600;
    font-size: 28px;
    letter-spacing: 23px;
    color: var(--ink-light);
  }
  .contact {
    position: absolute;
    left: 525px; top: 355px;
    width: 555px;
    margin: 0;
    padding: 0;
    list-style: none;
    text-align: center;
    font-family: "Tinos", serif;
    font-size: 38px;
    line-height: 60px;
    color: var(--ink-light);
  }
  .address {
    position: absolute;
    left: 525px; top: 628px;
    width: 650px;
    margin: 0;
    text-align: center;
    font-family: "Tinos", serif;
    font-size: 25px;
    color: var(--ink-light);
  }
</style>
</head>
<body>
  <main class="card">
    <div class="side-panel">
      <div class="side-strip"></div>
      <div class="ornament-left" role="img" aria-label="Decorative swirling flourish in blue and magenta"></div>
      <div class="brand">LANTERNYARD STUDIO</div>
    </div>
    <div class="ornament-right" role="img" aria-label="Faint decorative swirl flourish"></div>

    <header class="person">
      <h1 class="person-name">DALE FURNOW</h1>
      <p class="person-title">PRODUCER</p>
    </header>

    <ul class="contact">
      <li>c. 949-555-0164</li>
      <li>f. 650-555-0193</li>
      <li>dalef@lanternyardstudio.example</li>
    </ul>

    <p class="address">318 W Calle Norvista #2715, San Clemente, CA 92631</p>
  </main>
</body>
</html>
```